Business Coaching Model and Flow Chart

We need this flowchart, attached, to be updated in a modern and engaging way. This flowchart is the cornerstone of a business coaching class we are running, and will be the main support reference for the people who take the class. We are open to ideas as to how it is presented, but we would like a largely minimalist look that leaves space to be impactful where the key information sites. Our colour scheme is primary red (D51C29), white, grey (333333), black, and secondary green (3C8740). We will also need our logo present (attached).

```html
<!DOCTYPE html>
<html lang="en">
<head>
<meta charset="utf-8">
<title>Groups to Teams Through Learning Together</title>
<link href="https://fonts.googleapis.com/css2?family=Montserrat:wght@400;500;600;700;800&display=swap" rel="stylesheet">
<style>
  :root {
    --red: #D51C29;
    --green: #3C8740;
    --grey: #333333;
    --soft-grey: #8a8a8a;
    --black: #111111;
    --white: #ffffff;
    --paper: #fbfbfb;
    --red-tint: #f6d3d5;
    --green-tint: #d5e7d6;
  }
  * { margin: 0; padding: 0; box-sizing: border-box; }
  html, body { width: 1200px; height: 813px; overflow: hidden; background: var(--paper); }
  body { font-family: "Montserrat", sans-serif; color: var(--grey); position: relative; }

  .header-band { position: absolute; left: 0; top: 23px; width: 1200px; height: 76px; background: var(--green); }
  .title { position: absolute; left: 61px; top: 45px; font-size: 27px; font-weight: 800; letter-spacing: -0.3px; line-height: 32px; color: var(--grey); white-space: nowrap; }
  .title .lead { color: var(--white); }
  .presented { position: absolute; left: 903px; top: 54px; font-size: 15px; font-weight: 500; color: var(--white); padding-bottom: 4px; border-bottom: 2px solid var(--white); width: 93px; }
  .brand-bump { position: absolute; left: 991px; top: 25px; width: 128px; height: 128px; border-radius: 50%; background: var(--green); }
  .brand-dot { position: absolute; left: 1013px; top: 34px; width: 82px; height: 82px; border-radius: 50%; background: var(--red); }
  .brand-name { position: absolute; left: 991px; top: 117px; width: 128px; text-align: center; font-size: 9.5px; font-weight: 800; color: var(--red); letter-spacing: 0.3px; }

  .timeline { position: absolute; left: 0; top: 0; }

  .step-box { position: absolute; width: 50px; height: 46px; border-radius: 3px; color: var(--white); font-weight: 700; font-size: 17px; display: flex; align-items: center; justify-content: center; }
  .step-box.red { background: var(--red); }
  .step-box.green { background: var(--green); }

  .icon-slot { position: absolute; width: 48px; height: 48px; border-radius: 8px; }
  .icon-slot.red { background: var(--red-tint); }
  .icon-slot.green { background: var(--green-tint); }

  .stage { position: absolute; }
  .stage h2 { font-size: 18px; font-weight: 800; line-height: 22px; white-space: nowrap; }
  .stage .sub { font-size: 17px; font-weight: 400; line-height: 22px; white-space: nowrap; }
  .stage.red h2, .stage.red .sub { color: var(--red); }
  .stage.green h2, .stage.green .sub { color: var(--green); }

  .points { list-style: none; position: absolute; }
  .points li { position: relative; font-size: 12px; font-weight: 700; line-height: 14.6px; margin-bottom: 9.2px; padding-left: 16px; color: var(--grey); white-space: nowrap; }
  .points li::before { content: ""; position: absolute; left: 0; top: 3.3px; width: 8px; height: 8px; border-radius: 50%; background: var(--black); }
  .points.red li::before { background: var(--red); left: -5px; }
  .points.green li::before { background: var(--green); left: -7px; }
  .points.tight li { margin-bottom: 6.2px; }

  .details { list-style: none; position: absolute; }
  .details li { position: relative; font-size: 10px; font-weight: 500; line-height: 15.2px; color: var(--soft-grey); padding-left: 11px; white-space: nowrap; }
  .details li::before { content: ""; position: absolute; left: 0; top: 5.6px; width: 4.5px; height: 4.5px; border-radius: 50%; background: #aaaaaa; }
</style>
</head>
<body>

<div class="header-band"></div>
<div class="brand-bump"></div>
<h1 class="title"><span class="lead">GROUPS TO TEAMS</span> THROUGH LEARNING TOGETHER</h1>
<div class="presented">Presented By</div>
<div class="brand-dot"></div>
<div class="brand-name">MARA ELLISON</div>

<svg class="timeline" width="1200" height="813" viewBox="0 0 1200 813" aria-hidden="true">
  <defs>
    <linearGradient id="shift" x1="359" y1="0" x2="527" y2="0" gradientUnits="userSpaceOnUse">
      <stop offset="0" stop-color="#D51C29"/>
      <stop offset="1" stop-color="#3C8740"/>
    </linearGradient>
  </defs>
  <g stroke-width="3" fill="none">
    <line x1="106" y1="297" x2="106" y2="443" stroke="#D51C29"/>
    <line x1="359" y1="297" x2="359" y2="443" stroke="#D51C29"/>
    <line x1="230" y1="443" x2="230" y2="549" stroke="#D51C29"/>
    <line x1="527" y1="443" x2="527" y2="549" stroke="#3C8740"/>
    <line x1="667" y1="297" x2="667" y2="443" stroke="#3C8740"/>
    <line x1="807" y1="443" x2="807" y2="549" stroke="#3C8740"/>
    <line x1="948" y1="297" x2="948" y2="443" stroke="#3C8740"/>
  </g>
  <g stroke-width="5">
    <line x1="106" y1="443" x2="359" y2="443" stroke="#D51C29"/>
    <line x1="359" y1="443" x2="527" y2="443" stroke="url(#shift)"/>
    <line x1="527" y1="443" x2="948" y2="443" stroke="#3C8740"/>
  </g>
  <path d="M160 433 L182 443 L160 453 L166 443 Z" fill="#D51C29"/>
  <path d="M734 433 L756 443 L734 453 L740 443 Z" fill="#3C8740"/>
  <g>
    <circle cx="106" cy="443" r="10" fill="#D51C29"/>
    <circle cx="230" cy="443" r="10" fill="#D51C29"/>
    <circle cx="359" cy="443" r="10" fill="#D51C29"/>
    <circle cx="527" cy="443" r="10" fill="#3C8740"/>
    <circle cx="667" cy="443" r="10" fill="#3C8740"/>
    <circle cx="807" cy="443" r="10" fill="#3C8740"/>
    <circle cx="948" cy="443" r="10" fill="#3C8740"/>
  </g>
</svg>

<!-- step numbers -->
<div class="step-box red" style="left:81px; top:252px;">1</div>
<div class="step-box red" style="left:334px; top:252px;">3</div>
<div class="step-box green" style="left:642px; top:252px;">5</div>
<div class="step-box green" style="left:924px; top:252px;">7</div>
<div class="step-box red" style="left:205px; top:549px;">2</div>
<div class="step-box green" style="left:502px; top:549px;">4</div>
<div class="step-box green" style="left:783px; top:549px;">6</div>

<!-- stage icons -->
<div class="icon-slot red" style="left:82px; top:196px;" role="img" aria-label="Icon of a hand holding a maze"></div>
<div class="icon-slot red" style="left:335px; top:196px;" role="img" aria-label="Icon of a strategy easel"></div>
<div class="icon-slot green" style="left:643px; top:196px;" role="img" aria-label="Icon of a learner at a laptop"></div>
<div class="icon-slot green" style="left:924px; top:196px;" role="img" aria-label="Icon of a light bulb with puzzle pieces"></div>
<div class="icon-slot red" style="left:206px; top:608px;" role="img" aria-label="Icon of a magnifier and rising bar chart"></div>
<div class="icon-slot green" style="left:503px; top:608px;" role="img" aria-label="Icon of a gear and wrench"></div>
<div class="icon-slot green" style="left:784px; top:608px;" role="img" aria-label="Icon of three stars in a cycle"></div>

<!-- 1 Problem -->
<section class="stage red" style="left:148px; top:193px;">
  <h2>PROBLEM</h2>
</section>
<ul class="points red" style="left:157px; top:221px;">
  <li>Under-billing</li>
  <li>Staff Retention</li>
  <li>Hard To Recruit</li>
  <li>Client Complaints</li>
  <li>Staff Stress And Burnout</li>
  <li>Conflict</li>
  <li>Sector Constant Change</li>
  <li>Limited In Best Practice</li>
</ul>

<!-- 3 Planning -->
<section class="stage red" style="left:398px; top:193px;">
  <h2>Planning for success</h2>
  <p class="sub">(Make a Plan)</p>
</section>
<ul class="points" style="left:403px; top:247px;">
  <li>Team Data Analysis<br>Workshop</li>
  <li>Individual Development<br>Plan</li>
  <li>Team Development<br>Plan</li>
  <li>Organizational Plan</li>
</ul>

<!-- 5 Doing -->
<section class="stage green" style="left:702px; top:193px;">
  <h2>Doing</h2>
  <p class="sub">(Mastering the Tools)</p>
</section>
<ul class="points" style="left:705px; top:249px;">
  <li>Group Coaching</li>
  <li>Team Coaching</li>
  <li>Individual Coaching</li>
  <li>Peer Learning</li>
  <li>Lunch ‘N Learn</li>
</ul>

<!-- 7 Solution -->
<section class="stage green" style="left:984px; top:193px;">
  <h2>SOLUTION</h2>
</section>
<ul class="points green" style="left:991px; top:221px;">
  <li>Self Awareness &amp;<br>Ownership</li>
  <li>Partnership</li>
  <li>Great Place To Work</li>
  <li>Growth Mindset</li>
  <li>Coach Approaching<br>Culture</li>
  <li>Feedback Culture</li>
  <li>Way To Manage<br>Conflict</li>
  <li>Best Practice<br>Communication Skills</li>
</ul>

<!-- 2 Clarify -->
<section class="stage red" style="left:272px; top:545px;">
  <h2>Clarify Challenges</h2>
  <p class="sub">(Diagnostics)</p>
</section>
<ul class="points" style="left:284px; top:593px;">
  <li>Scoping</li>
  <li>Interviews</li>
  <li>Group Reflection</li>
  <li>Opinion Surveys</li>
  <li>Certified Assessments</li>
</ul>
<ul class="details" style="left:309px; top:709px;">
  <li>Personality Styles</li>
  <li>Work Preference</li>
  <li>Strengths &amp; Values</li>
  <li>Trust</li>
  <li>360</li>
</ul>

<!-- 4 Learn -->
<section class="stage green" style="left:567px; top:545px;">
  <h2>Learn The Tools</h2>
  <p class="sub">(Workshops)</p>
</section>
<ul class="points" style="left:569px; top:602px;">
  <li>Foundation Workshops</li>
</ul>
<ul class="details" style="left:594px; top:616px;">
  <li>Difficult Conversations</li>
  <li>Giving &amp; Receiving Feedback</li>
  <li>Values Alignment</li>
  <li>Shared Purpose</li>
  <li>Ways Of Working</li>
  <li>Diversity</li>
  <li>Well-being</li>
  <li>Time Management</li>
</ul>
<ul class="points" style="left:569px; top:756px;">
  <li>Customized Workshops</li>
</ul>

<!-- 6 Reflect -->
<section class="stage green" style="left:851px; top:545px;">
  <h2>Reflect-Adapt-Embed</h2>
</section>
<ul class="points tight" style="left:853px; top:570px;">
  <li>Culture Committee</li>
  <li>Embedding Workshop</li>
  <li>Culture Collateral</li>
  <li>WOW Manifesto</li>
  <li>Leadership Team Coaching</li>
  <li>Measure ROI</li>
  <li>Review Success</li>
  <li>Evaluation Surveys</li>
  <li>Temperature Checks</li>
  <li>Recruit To Suit</li>
  <li>Future Proofing - What Next?</li>
</ul>

</body>
</html>
```